Brightfield Optics seeks updated contemporary business card

Brightfield Optics utilizes advanced technology and we take pride in the modern look and feel of our practice. We like our current card, but it's been four years so it is time for an update.

Target Market(s)

Females 25-45 make the most health care decisions for their family.

Contact Information for Business Card

Clean front. Back with info and with empty space for appointment time or other small note

Requirements
Must have
• Logo
Ridge Marketvale, 28413 E Larkspur Ave
Cedar Terrace Marketvale, 4638 S Dunmore Rd
Call or text: 509-342-1968
email: hello@brightfieldoptics.example
brightfieldoptics.example
Dr Tobias Werring & Associates

```html
<!DOCTYPE html>
<html lang="en">
<head>
<meta charset="utf-8">
<title>Brightfield Optics – Business Card</title>
<link rel="stylesheet" href="https://fonts.googleapis.com/css2?family=Montserrat:wght@400;500;600&family=Ubuntu:wght@500;700&display=swap">
<style>
  :root {
    --navy: #2b3f73;
    --blue: #0a8fcf;
    --blue-deep: #0577b3;
    --grey-text: #686b70;
    --grey-rule: #b9bbbe;
    --card: #ffffff;
    --backdrop: #e3e3e3;
  }
  * { box-sizing: border-box; margin: 0; padding: 0; }
  html, body { width: 1200px; height: 800px; overflow: hidden; }
  body {
    background: var(--backdrop);
    font-family: "Montserrat", sans-serif;
    position: relative;
  }
  .card {
    position: absolute;
    background: var(--card);
    box-shadow: 0 14px 30px rgba(0,0,0,0.18);
    overflow: hidden;
  }

  /* Info side (portrait) */
  .card--info {
    left: 110px; top: 95px;
    width: 360px; height: 610px;
    padding: 44px 34px 30px;
    display: flex; flex-direction: column; align-items: center;
  }
  .brand {
    display: flex; align-items: center; gap: 10px;
  }
  .brand__dot {
    width: 22px; height: 22px; border-radius: 50%;
    background: var(--blue);
  }
  .brand__name {
    font-family: "Ubuntu", sans-serif;
    font-weight: 700;
    color: var(--navy);
    font-size: 26px;
    letter-spacing: 0.5px;
    text-transform: uppercase;
  }
  .doctor {
    margin-top: 26px;
    font-family: "Ubuntu", sans-serif;
    font-weight: 500;
    font-size: 30px;
    color: var(--navy);
    white-space: nowrap;
  }
  .doctor__title { color: var(--blue); }
  .doctor__suffix {
    align-self: flex-end;
    margin-right: 10px;
    margin-top: -2px;
    font-size: 13px;
    color: var(--grey-text);
  }
  .divider {
    width: 100%;
    display: flex; align-items: center; gap: 10px;
    margin-top: 18px;
  }
  .divider__rule { flex: 1; height: 1px; background: var(--blue-deep); }
  .divider__rule--navy { background: var(--navy); }
  .icon {
    width: 22px; height: 22px; border-radius: 50%;
    background: var(--blue-deep);
    display: flex; align-items: center; justify-content: center;
  }
  .icon svg { width: 13px; height: 13px; }
  .icon-group { display: flex; gap: 7px; }
  .contact {
    margin-top: 14px;
    text-align: center;
    color: var(--grey-text);
    font-size: 15px;
    line-height: 1.55;
  }
  .address {
    margin-top: 14px;
    text-align: center;
    color: var(--grey-text);
    font-size: 15px;
    line-height: 1.5;
  }
  .rule-full {
    width: 100%; height: 1px; background: var(--blue-deep);
    margin-top: 20px;
  }
  .appointment {
    width: 100%;
    margin-top: 14px;
    position: relative;
  }
  .appointment__label {
    text-align: right;
    font-size: 11px;
    font-weight: 600;
    letter-spacing: 0.5px;
    color: var(--grey-text);
  }
  .field {
    display: flex; align-items: flex-end; gap: 8px;
    margin-top: 14px;
  }
  .field__label {
    font-size: 12px;
    font-weight: 500;
    color: var(--navy);
  }
  .field__line { flex: 1; height: 1px; background: var(--grey-rule); margin-bottom: 3px; }
  .field-row { display: flex; gap: 14px; }
  .field-row .field { flex: 1; }

  /* Front side (landscape) */
  .card--front {
    left: 530px; top: 230px;
    width: 600px; height: 340px;
  }
  .front__band {
    position: absolute; left: 0; top: 0; bottom: 0;
    width: 150px;
    background: linear-gradient(180deg, var(--blue-deep), var(--blue));
  }
  .front__brand {
    position: absolute;
    left: 150px; right: 0; top: 0; bottom: 0;
    display: flex; align-items: center; justify-content: center;
  }
  .front__brand .brand__name { font-size: 34px; }
  .front__brand .brand__dot { width: 28px; height: 28px; }
</style>
</head>
<body>

  <section class="card card--info" aria-label="Card back with contact details">
    <div class="brand">
      <span class="brand__dot"></span>
      <span class="brand__name">Brightfield Optics</span>
    </div>

    <h1 class="doctor"><span class="doctor__title">Dr</span> Tobias Werring</h1>
    <p class="doctor__suffix">Associates</p>

    <div class="divider">
      <span class="divider__rule divider__rule--navy"></span>
      <div class="icon-group">
        <span class="icon" aria-label="Phone">
          <svg viewBox="0 0 16 16"><path fill="#fff" d="M4 1.5l2 3-1.3 1.3c.8 1.8 2.2 3.2 4 4L10 8.5l3 2-1 2.5c-5 0-9.5-4.5-9.5-9.5z"/></svg>
        </span>
        <span class="icon" aria-label="Email">
          <svg viewBox="0 0 16 16"><rect x="2" y="4" width="12" height="8" fill="#fff"/><path d="M2 4l6 4.5L14 4" fill="none" stroke="#0577b3" stroke-width="1.2"/></svg>
        </span>
        <span class="icon" aria-label="Website">
          <svg viewBox="0 0 16 16" fill="none" stroke="#fff" stroke-width="1.3"><circle cx="8" cy="8" r="5.5"/><path d="M2.5 8h11M8 2.5c2 2 2 9 0 11M8 2.5c-2 2-2 9 0 11"/></svg>
        </span>
      </div>
      <span class="divider__rule"></span>
    </div>

    <div class="contact">
      <p>509-342-1968</p>
      <p>hello@brightfieldoptics.example</p>
      <p>www.brightfieldoptics.example</p>
    </div>

    <div class="divider">
      <span class="divider__rule"></span>
      <span class="icon" aria-label="Location">
        <svg viewBox="0 0 16 16"><path fill="#fff" d="M8 1.5a4.5 4.5 0 0 0-4.5 4.5C3.5 9.5 8 14.5 8 14.5s4.5-5 4.5-8.5A4.5 4.5 0 0 0 8 1.5z"/><circle cx="8" cy="6" r="1.7" fill="#0577b3"/></svg>
      </span>
      <span class="divider__rule"></span>
    </div>

    <div class="address">
      <p>Ridge Marketvale, 28413 E Larkspur Ave</p>
      <p>Cedar Terrace Marketvale,</p>
      <p>4638 S Dunmore Rd</p>
    </div>

    <span class="rule-full"></span>

    <div class="appointment">
      <p class="appointment__label">APPOINTMENT</p>
      <div class="field">
        <span class="field__label">Name</span><span class="field__line"></span>
      </div>
      <div class="field-row">
        <div class="field"><span class="field__label">Date</span><span class="field__line"></span></div>
        <div class="field"><span class="field__label">Time</span><span class="field__line"></span></div>
      </div>
    </div>
  </section>

  <section class="card card--front" aria-label="Card front">
    <div class="front__band"></div>
    <div class="front__brand">
      <div class="brand">
        <span class="brand__dot"></span>
        <span class="brand__name">Brightfield Optics</span>
      </div>
    </div>
  </section>

</body>
</html>
```